School Hallway Magnetic Display Design for school values

I am looking for a someone to help me design a magnetic hallway display that will hang in the hallway of our small school. There are several elements, including 1. 6ft by 4ft designed magnetic bulletin board, 2. Magnets that will stick to the board. See attachment for which elements belong where. The display will be for our TAVRON program, which rewards students for demonstrating our school values. We want the display to be beautiful and interactive. We are also rebranding, so we want the design to align with our new fonts and colors. In the attached PDF is an outline of our new brand guidelines. Unfortunately, we don't have the color codes, but I'm hoping that you can match the colors listed. Attached are elements to be used on the board, but please use your creativity to make it more dynamic and visually appealing. For example, the star magnets could be another shape. The TAVRON magnets must remain the same. I've included two photos of boards at other schools that inspired this project.

Target Market(s)

School Community

Industry/Entity Type

Education

Requirements
Should not have
• School Logo

```html
<!DOCTYPE html>
<html lang="en">
<head>
<meta charset="utf-8">
<title>TAVRON of the Month – Hallway Board</title>
<link rel="stylesheet" href="https://fonts.googleapis.com/css2?family=Poppins:wght@600;800;900&family=Raleway:wght@800;900&display=swap">
<style>
  :root {
    --bg: #eceef1;
    --white: #ffffff;
    --navy: #2b2f8f;
    --blue: #1e78d4;
    --green: #5cbf3a;
    --purple: #7a3aa8;
    --pink: #ea5a9a;
    --orange: #f07a28;
    --teal: #18a5a0;
    --yellow: #f9c81e;
    --red: #ef4a43;
    --glass: #cfe6f7;
    --board-edge: #dcdfe4;
  }
  * { box-sizing: border-box; margin: 0; padding: 0; }
  html, body { width: 1200px; height: 1200px; overflow: hidden; }
  body { background: var(--bg); font-family: "Poppins", sans-serif; position: relative; }

  .board {
    position: absolute; left: 40px; top: 92px; width: 1120px; height: 1016px;
    background: linear-gradient(135deg, var(--blue) 0%, var(--pink) 30%, var(--yellow) 55%, var(--green) 75%, var(--orange) 100%);
    box-shadow: 0 6px 18px rgba(0,0,0,.12);
  }
  .board-inner {
    position: absolute; left: 33px; top: 210px; width: 1053px; height: 764px;
    background: var(--white);
  }
  .title-band {
    position: absolute; left: 87px; top: 51px; width: 952px; height: 117px;
    background: var(--white);
    display: flex; align-items: center; justify-content: center; gap: 18px;
  }
  .title-word { font-family: "Poppins", sans-serif; font-weight: 900; font-size: 96px; line-height: 1; letter-spacing: 2px; }
  .title-small { display: flex; flex-direction: column; font-weight: 800; font-size: 30px; line-height: 1; color: var(--navy); text-align: center; }
  .c-blue { color: var(--blue); } .c-pink { color: var(--pink); } .c-yellow { color: var(--yellow); }
  .c-green { color: var(--green); } .c-purple { color: var(--purple); } .c-orange { color: var(--orange); }
  .c-teal { color: var(--teal); } .c-navy { color: var(--navy); } .c-red { color: var(--red); }

  .values { position: absolute; left: 45px; top: 225px; width: 326px; list-style: none; }
  .value-card {
    height: 106px; margin-bottom: 17px; border-radius: 6px;
    display: flex; align-items: center; justify-content: center;
    font-family: "Raleway", sans-serif; font-weight: 900; font-size: 42px; color: var(--white);
    -webkit-text-stroke: 1.5px var(--navy); paint-order: stroke fill;
    text-shadow: 0 3px 0 rgba(30,30,80,.55);
    box-shadow: 0 3px 6px rgba(0,0,0,.15);
  }
  .value-card.small { font-size: 36px; }
  .v-blue { background: var(--blue); } .v-green { background: var(--green); }
  .v-purple { background: var(--purple); } .v-pink { background: var(--pink); }
  .v-orange { background: var(--orange); } .v-teal { background: var(--teal); }

  .feature-panel {
    position: absolute; left: 386px; top: 223px; width: 486px; height: 439px;
    background: linear-gradient(160deg, #ffffff, #eef0f2);
    border: 1px solid var(--board-edge);
  }

  .magnets {
    position: absolute; left: 395px; top: 690px; width: 456px; height: 274px;
    display: grid; grid-template-columns: repeat(5, 1fr); grid-template-rows: repeat(3, 1fr);
    place-items: center;
  }
  .magnet { width: 72px; height: 72px; border-radius: 50%; }
  .magnet.shield { border-radius: 10px 10px 36px 36px; }
  .m-star { background: linear-gradient(135deg, var(--yellow), var(--pink), var(--blue)); }
  .m-sun { background: var(--yellow); }
  .m-sun2 { background: var(--orange); }
  .m-sun3 { background: var(--pink); }
  .m-sun4 { background: var(--blue); }
  .m-shield1 { background: var(--purple); }
  .m-shield2 { background: var(--pink); }
  .m-shield3 { background: var(--teal); }
  .m-ribbon { background: linear-gradient(180deg, var(--yellow), var(--teal)); }

  .progress { position: absolute; left: 882px; top: 223px; width: 223px; height: 770px; }
  .progress-label {
    position: absolute; top: 12px; left: 0; width: 100%;
    text-align: center; font-weight: 600; font-size: 17px; line-height: 1.15; color: var(--navy);
  }
  .progress svg { position: absolute; left: 0; top: 60px; }
</style>
</head>
<body>
  <main class="board" aria-label="TAVRON of the Month magnetic board">
    <div class="board-inner"></div>

    <header class="title-band">
      <h1 class="title-word" aria-label="TAVRON">
        <span class="c-blue">T</span><span class="c-pink">A</span><span class="c-yellow">V</span><span class="c-green">R</span><span class="c-purple">O</span><span class="c-orange">N</span>
      </h1>
      <div class="title-small"><span>OF</span><span>THE</span></div>
      <div class="title-word" aria-label="MONTH">
        <span class="c-yellow">M</span><span class="c-navy">O</span><span class="c-pink">N</span><span class="c-teal">T</span><span class="c-orange">H</span>
      </div>
    </header>

    <ul class="values">
      <li class="value-card v-blue">SIMPLICITY</li>
      <li class="value-card v-green">PEACE</li>
      <li class="value-card v-purple">INTEGRITY</li>
      <li class="value-card v-pink small">COMMUNITY</li>
      <li class="value-card v-orange">EQUALITY</li>
      <li class="value-card v-teal small">STEWARDSHIP</li>
    </ul>

    <section class="feature-panel" aria-label="Magnetic whiteboard area"></section>

    <section class="magnets" aria-label="Reward magnets">
      <div class="magnet m-star" role="img" aria-label="Star magnet"></div>
      <div class="magnet m-sun" role="img" aria-label="Sun magnet"></div>
      <div class="magnet m-sun4" role="img" aria-label="Sun magnet"></div>
      <div class="magnet shield m-shield1" role="img" aria-label="Shield magnet"></div>
      <div class="magnet shield m-shield2" role="img" aria-label="Shield magnet"></div>
      <div class="magnet m-star" role="img" aria-label="Star magnet"></div>
      <div class="magnet m-sun2" role="img" aria-label="Sun magnet"></div>
      <div class="magnet m-sun3" role="img" aria-label="Sun magnet"></div>
      <div class="magnet shield m-shield3" role="img" aria-label="Shield magnet"></div>
      <div class="magnet shield m-shield2" role="img" aria-label="Shield magnet"></div>
      <div class="magnet m-ribbon" role="img" aria-label="Ribbon award magnet"></div>
      <div class="magnet m-ribbon" role="img" aria-label="Ribbon award magnet"></div>
      <div class="magnet m-ribbon" role="img" aria-label="Ribbon award magnet"></div>
      <div class="magnet m-ribbon" role="img" aria-label="Ribbon award magnet"></div>
      <div class="magnet m-ribbon" role="img" aria-label="Ribbon award magnet"></div>
    </section>

    <section class="progress" aria-label="Participation progress meter">
      <p class="progress-label">Participation<br>Progress</p>
      <svg width="223" height="700" viewBox="0 0 223 700">
        <!-- tick stars -->
        <g fill="var(--red)"><polygon points="0,0 4,-11 8,0 -3,-7 11,-7" transform="translate(6,136)"/></g>
        <g fill="var(--blue)"><polygon points="0,0 4,-11 8,0 -3,-7 11,-7" transform="translate(6,213)"/></g>
        <g fill="var(--yellow)"><polygon points="0,0 4,-11 8,0 -3,-7 11,-7" transform="translate(6,289)"/></g>
        <g fill="var(--green)"><polygon points="0,0 4,-11 8,0 -3,-7 11,-7" transform="translate(6,366)"/></g>
        <g fill="var(--purple)"><polygon points="0,0 4,-11 8,0 -3,-7 11,-7" transform="translate(6,442)"/></g>
        <!-- tube -->
        <path d="M82,60 a28,28 0 0 1 56,0 V520 a66,66 0 1 1 -56,0 Z" fill="var(--glass)" stroke="var(--navy)" stroke-width="6"/>
        <rect x="96" y="262" width="28" height="300" fill="var(--red)"/>
        <circle cx="110" cy="576" r="54" fill="var(--red)"/>
        <!-- ticks -->
        <g stroke="var(--navy)" stroke-width="3">
          <line x1="30" y1="130" x2="150" y2="130"/><line x1="30" y1="207" x2="150" y2="207"/>
          <line x1="30" y1="283" x2="150" y2="283"/><line x1="30" y1="360" x2="150" y2="360"/>
          <line x1="30" y1="436" x2="150" y2="436"/>
          <line x1="40" y1="150" x2="66" y2="150"/><line x1="40" y1="170" x2="66" y2="170"/><line x1="40" y1="188" x2="66" y2="188"/>
          <line x1="40" y1="227" x2="66" y2="227"/><line x1="40" y1="246" x2="66" y2="246"/><line x1="40" y1="265" x2="66" y2="265"/>
          <line x1="40" y1="303" x2="66" y2="303"/><line x1="40" y1="322" x2="66" y2="322"/><line x1="40" y1="341" x2="66" y2="341"/>
          <line x1="40" y1="380" x2="66" y2="380"/><line x1="40" y1="398" x2="66" y2="398"/><line x1="40" y1="417" x2="66" y2="417"/>
          <line x1="40" y1="456" x2="66" y2="456"/><line x1="40" y1="475" x2="66" y2="475"/>
        </g>
      </svg>
    </section>
  </main>
</body>
</html>
```